TalkBloom - Language Coaching Services

Sleek, innovative, trendy design for Language Coaching business.

TalkBloom is a new UK based company that provides Language Coaching services. We offer highly personalized on-line and face to face language courses. We also impart learning techniques workshops based on the latest neuroscience research for second-language acquisition.

Target Market(s)

Industry/Entity Type

Consulting

Contact Information for Business Card

TalkBloom
DaniraQT@talkbloom.co.uk
TalkBloom.co.uk
London, UK

Font styles to use
Sans Serif

```html
<!DOCTYPE html>
<html lang="en">
<head>
<meta charset="utf-8">
<title>TalkBloom Business Cards</title>
<link href="https://fonts.googleapis.com/css2?family=Open+Sans:wght@400;600;700&display=swap" rel="stylesheet">
<style>
  :root {
    --bg: #e9e6e2;
    --card: #2b2b2d;
    --card-edge: #232325;
    --blue: #1b97d2;
    --white: #f4f4f4;
    --muted: #d9d9d9;
  }
  * { margin: 0; padding: 0; box-sizing: border-box; }
  html, body { width: 1200px; height: 900px; overflow: hidden; }
  body {
    background: var(--bg);
    font-family: "Open Sans", Arial, sans-serif;
    position: relative;
  }
  .card {
    position: absolute;
    left: 280px;
    width: 640px;
    height: 366px;
    background: linear-gradient(160deg, var(--card) 0%, var(--card-edge) 100%);
    border-radius: 22px;
    overflow: hidden;
    box-shadow: 0 14px 30px rgba(0,0,0,.25);
  }
  .card--front { top: 46px; }
  .card--back { top: 448px; }

  .brand {
    display: flex;
    align-items: center;
    gap: 18px;
    color: var(--blue);
    font-weight: 700;
    letter-spacing: 1px;
  }
  .brand-mark {
    border: 6px solid var(--blue);
    border-radius: 50%;
    flex: none;
  }

  .card--front .brand {
    position: absolute;
    left: 0; right: 0; top: 70px;
    flex-direction: column;
    gap: 20px;
    font-size: 64px;
    line-height: 1;
  }
  .card--front .brand-mark { width: 104px; height: 104px; }
  .front-url {
    position: absolute;
    left: 0; right: 0; top: 290px;
    text-align: center;
    color: var(--white);
    font-size: 20px;
    font-weight: 600;
  }

  .card--back .brand {
    position: absolute;
    left: 46px; top: 34px;
    font-size: 40px;
  }
  .card--back .brand-mark { width: 74px; height: 74px; border-width: 5px; }

  .contact-name {
    position: absolute;
    left: 50px; top: 152px;
    color: var(--blue);
    font-size: 20px;
    font-weight: 700;
  }
  .contact-list {
    position: absolute;
    left: 50px; top: 196px;
    list-style: none;
  }
  .contact-list li {
    display: flex;
    align-items: center;
    gap: 16px;
    height: 30px;
    color: var(--white);
    font-size: 18px;
  }
  .contact-list svg { width: 20px; height: 20px; flex: none; fill: var(--blue); }

  .card-band {
    position: absolute;
    left: 0; right: 0; bottom: 0;
    height: 16px;
    background: var(--blue);
  }
</style>
</head>
<body>
  <section class="card card--front">
    <div class="brand"><span class="brand-mark"></span><span class="brand-name">TalkBloom</span></div>
    <p class="front-url">www.talkbloom.co.uk</p>
  </section>

  <section class="card card--back">
    <div class="brand"><span class="brand-mark"></span><span class="brand-name">TalkBloom</span></div>
    <p class="contact-name">TalkBloom</p>
    <ul class="contact-list">
      <li>
        <svg viewBox="0 0 24 24" aria-hidden="true"><path d="M6.6 10.8c1.4 2.8 3.8 5.2 6.6 6.6l2.2-2.2c.3-.3.7-.4 1-.2 1.1.4 2.3.6 3.6.6.6 0 1 .4 1 1V20c0 .6-.4 1-1 1C10.6 21 3 13.4 3 4c0-.6.4-1 1-1h3.5c.6 0 1 .4 1 1 0 1.3.2 2.5.6 3.6.1.3 0 .7-.2 1z"/></svg>
        <span>+44 1632 960718</span>
      </li>
      <li>
        <svg viewBox="0 0 24 24" aria-hidden="true"><path d="M2 5h20v14H2z M3.5 6.5 12 13l8.5-6.5" fill="none" stroke="#1b97d2" stroke-width="2"/></svg>
        <span>daniraqt@talkbloom.co.uk</span>
      </li>
      <li>
        <svg viewBox="0 0 24 24" aria-hidden="true"><circle cx="12" cy="12" r="10"/><path d="M2 12h20M12 2c3 3 3 17 0 20M12 2c-3 3-3 17 0 20" fill="none" stroke="#2b2b2d" stroke-width="1.5"/></svg>
        <span>www.talkbloom.co.uk</span>
      </li>
      <li>
        <svg viewBox="0 0 24 24" aria-hidden="true"><path d="M12 2a7 7 0 0 0-7 7c0 5 7 13 7 13s7-8 7-13a7 7 0 0 0-7-7zm0 9.5A2.5 2.5 0 1 1 12 6.5a2.5 2.5 0 0 1 0 5z"/></svg>
        <span>London, UK</span>
      </li>
    </ul>
    <div class="card-band"></div>
  </section>
</body>
</html>
```